Company Stationary

I'd like a template to use for company stationery. We frequently write short 1 - 2 page Word documents (which we save as PDF) to clients and prospects and the presentation is boring and doesn't look professional. I am looking for a Word template that will convey a better sense of professionalism. The design should include our logo (attached) but be simple and elegant. It should save nicely as a PDF, since that is how we will send the files via email.

Target Market(s)

Financial Institutions

Industry/Entity Type

Financial Service

Font styles to use
Serif

Colors

Designer to choose colors to be used in the design.

Requirements
Must have
• Simple design. Needs to be subtle. I don't want the design to be more interesting than the message we are writing.
Nice to have
• When the reader sees it, I want them to feel they are reading something published by a large, very successful company.
Should not have
• Not overpowering design and colors.

```html
<!DOCTYPE html>
<html lang="en">
<head>
<meta charset="utf-8">
<title>Veranta Capital – Letterhead</title>
<link rel="stylesheet" href="https://fonts.googleapis.com/css2?family=Open+Sans:wght@400;600;700&display=swap">
<style>
  :root {
    --backdrop: #d8d9d5;
    --paper: #ffffff;
    --brand-red: #e8202a;
    --brand-red-light: #f5484f;
    --rule-grey: #9a9a9a;
    --ink: #1b1b1b;
    --muted: #6f6f6f;
  }
  * { box-sizing: border-box; margin: 0; padding: 0; }
  html, body {
    width: 1200px; height: 784px; overflow: hidden;
    background: var(--backdrop);
    font-family: "Open Sans", Arial, sans-serif;
  }
  .canvas {
    position: relative; width: 1200px; height: 784px;
    display: flex; align-items: center; justify-content: center;
  }
  .letterhead {
    position: relative; width: 526px; height: 744px;
    background: var(--paper);
    box-shadow: 0 2px 10px rgba(0,0,0,.18);
    overflow: hidden;
  }
  .header-rule-red {
    position: absolute; top: 14px; left: 0; width: 150px; height: 4px;
    background: linear-gradient(90deg, var(--brand-red-light), var(--brand-red));
  }
  .brand {
    position: absolute; top: 34px; left: 170px;
    display: flex; align-items: center; gap: 8px;
  }
  .brand-mark { width: 10px; height: 10px; background: var(--brand-red); }
  .brand-name {
    font-size: 22px; font-weight: 700; color: var(--ink);
    letter-spacing: .3px;
  }
  .header-rule-grey {
    position: absolute; top: 74px; left: 330px; right: 0; height: 4px;
    background: linear-gradient(90deg, #c4c4c4, var(--rule-grey));
  }
  .contact-line {
    position: absolute; left: 14px; bottom: 46px;
    display: flex; align-items: center; gap: 5px;
    font-size: 7.5px; color: var(--muted); white-space: nowrap;
  }
  .contact-icon { width: 9px; height: 9px; flex: none; }
  .footer-rule-grey {
    position: absolute; left: 8px; width: 360px; bottom: 38px; height: 2px;
    background: var(--rule-grey);
  }
  .footer-rule-red {
    position: absolute; left: 0; width: 400px; bottom: 26px; height: 5px;
    background: var(--brand-red);
  }
  .footer-web {
    position: absolute; right: 0; bottom: 0; width: 118px; height: 38px;
    background: linear-gradient(90deg, var(--brand-red-light), var(--brand-red));
    color: #fff; font-size: 9px; font-weight: 600;
    display: flex; align-items: center; justify-content: center;
  }
</style>
</head>
<body>
<main class="canvas">
  <article class="letterhead">
    <div class="header-rule-red"></div>
    <div class="brand">
      <span class="brand-mark"></span>
      <span class="brand-name">Veranta Capital</span>
    </div>
    <div class="header-rule-grey"></div>

    <div class="contact-line">
      <svg class="contact-icon" viewBox="0 0 10 10"><circle cx="5" cy="5" r="5" fill="#e8202a"/><path d="M5 2a2 2 0 0 0-2 2c0 1.5 2 4 2 4s2-2.5 2-4a2 2 0 0 0-2-2z" fill="#fff"/></svg>
      <span>Example 15, 00000 for Example</span>
      <svg class="contact-icon" viewBox="0 0 10 10"><circle cx="5" cy="5" r="5" fill="#e8202a"/><rect x="3.5" y="2.2" width="3" height="5.6" rx=".6" fill="#fff"/></svg>
      <span>+00 00 00000000 2</span>
      <svg class="contact-icon" viewBox="0 0 10 10"><circle cx="5" cy="5" r="5" fill="#e8202a"/><rect x="2.5" y="3" width="5" height="4" fill="#fff"/></svg>
      <span>+00 00 00000000 0</span>
      <svg class="contact-icon" viewBox="0 0 10 10"><circle cx="5" cy="5" r="5" fill="#e8202a"/><rect x="2.4" y="3.2" width="5.2" height="3.6" fill="#fff"/><path d="M2.4 3.2 5 5.3 7.6 3.2" stroke="#e8202a" stroke-width=".6" fill="none"/></svg>
      <span>info@example.com</span>
    </div>
    <div class="footer-rule-grey"></div>
    <div class="footer-rule-red"></div>
    <div class="footer-web">www.example.com</div>
  </article>
</main>
</body>
</html>
```